business card for a shoe shop

we would like a business card for a family owned shoe shop.
With this information included.
Darnell's Shoe Store
Family owned since 1947

then on other side
Darnell's Shoe Store
Footwear fitting specialist
Phone: 9187 2630
218 Quarry St, Fernleigh Downs 3187
(cnr. Hartwick Rd and Quarry St)
darnellshoes218@examplemail.com
if could incorporate the purple color on card i have attached.

```html
<!DOCTYPE html>
<html lang="en">
<head>
<meta charset="utf-8">
<title>Darnell's Shoe Store – Business Card</title>
<link rel="stylesheet" href="https://fonts.googleapis.com/css2?family=Bebas+Neue&family=Lato:wght@400&display=swap">
<style>
  :root {
    --backdrop: #c0c0c0;
    --card-white: #ffffff;
    --brand-purple: #7561a8;
    --ink-purple: #6e58a6;
    --ink-white: #ffffff;
  }
  * { margin: 0; padding: 0; box-sizing: border-box; }
  html, body {
    width: 1200px; height: 1200px; overflow: hidden;
    background: var(--backdrop);
  }
  .canvas { position: relative; width: 1200px; height: 1200px; }

  .card { position: absolute; width: 823px; height: 474px; }
  .card--front { left: 188px; top: 91px; background: var(--card-white); }
  .card--back { left: 186px; top: 635px; width: 828px; background: var(--brand-purple); }

  .brand-name {
    position: absolute;
    font-family: "Bebas Neue", "Oswald", sans-serif;
    font-weight: 400;
    line-height: 1;
    white-space: nowrap;
    text-align: right;
    letter-spacing: 0.2px;
  }
  .tagline {
    position: absolute;
    font-family: "Lato", sans-serif;
    font-weight: 400;
    line-height: 1;
    white-space: nowrap;
    text-align: right;
  }

  .card--front .brand-name { right: 436px; top: 197px; font-size: 54px; color: var(--ink-purple); }
  .card--front .tagline { right: 436px; top: 253px; font-size: 21px; color: var(--ink-purple); }

  .divider {
    position: absolute; left: 410px; top: 186px;
    width: 2px; height: 102px; background: var(--ink-purple);
  }

  .contact-list {
    position: absolute; left: 436px; top: 184px;
    list-style: none;
    font-family: "Lato", sans-serif;
    font-size: 20px; line-height: 28px;
    color: var(--ink-purple);
    white-space: nowrap;
  }
  .contact-list li { display: flex; align-items: center; }
  .contact-icon {
    width: 16px; height: 18px; margin-right: 7px; flex: none;
    fill: var(--ink-purple);
  }
  .contact-icon--spacer { visibility: hidden; }

  .card--back .brand-name { right: 118px; top: 172px; font-size: 88px; color: var(--ink-white); }
  .card--back .tagline { right: 118px; top: 264px; font-size: 35px; color: var(--ink-white); }
</style>
</head>
<body>
<main class="canvas">

  <section class="card card--front" aria-label="Business card front">
    <h1 class="brand-name">Darnell's Shoe Store</h1>
    <p class="tagline">Footwear Fitting Specialist</p>
    <div class="divider"></div>
    <ul class="contact-list">
      <li>
        <svg class="contact-icon" viewBox="0 0 16 18" aria-hidden="true">
          <path d="M8 0C4.1 0 1.5 2.8 1.5 6.3 1.5 10.6 8 18 8 18s6.5-7.4 6.5-11.7C14.5 2.8 11.9 0 8 0zm0 9a2.6 2.6 0 1 1 0-5.2A2.6 2.6 0 0 1 8 9z"/>
        </svg>
        218 Quarry St, Fernleigh Downs 3187
      </li>
      <li>
        <svg class="contact-icon contact-icon--spacer" viewBox="0 0 16 18" aria-hidden="true"></svg>
        (cnr. Hartwick Rd and Quarry St)
      </li>
      <li>
        <svg class="contact-icon" viewBox="0 0 16 18" aria-hidden="true">
          <path d="M3.2 2.5l2.3-.4 1.4 3.4-1.6 1.2c.8 1.9 2.1 3.3 3.9 4.3l1.3-1.5 3.3 1.6-.5 2.3c-.2.8-1 1.3-1.8 1.1C6.4 13.4 2.8 9.6 2 4.3c-.1-.9.4-1.7 1.2-1.8z"/>
          <path d="M9.5 2.2a5 5 0 0 1 4.3 4.3l-1.1.1a3.9 3.9 0 0 0-3.3-3.3zM9.2 4.4a2.8 2.8 0 0 1 2.4 2.4l-1.1.1a1.7 1.7 0 0 0-1.4-1.4z"/>
        </svg>
        9187 2630
      </li>
      <li>
        <svg class="contact-icon" viewBox="0 0 16 18" aria-hidden="true">
          <path d="M1 5h14v9H1z M1.6 5.4L8 10l6.4-4.6" fill="none" stroke="var(--ink-purple)" stroke-width="1.6"/>
          <path d="M1 14l5-4.6M15 14l-5-4.6" stroke="var(--ink-purple)" stroke-width="1.4"/>
        </svg>
        darnellshoes218@examplemail.com
      </li>
    </ul>
  </section>

  <section class="card card--back" aria-label="Business card back">
    <h2 class="brand-name">Darnell's Shoe Store</h2>
    <p class="tagline">Family owned since 1947</p>
  </section>

</main>
</body>
</html>
```